Birchmead Assurance Group Ltd needs a business card and logo

We need a logo for documents, invoices etc and a business card to match. We are a health auditing, training and consulting company based in NZ and working in both Australia and NZ. We ensure health organisations meet all their compliance requirements and develop expertise in the health auditing sector. The design should in some way reflect either symbols for quality management in the health sector.

Target Market(s)

Health providers and those wishing to increase their capability in meeting and understanding compliance requirements

Industry/Entity Type

Business

Contact Information for Business Card

Logo plus contact details

Logo Text

Health auditing, consultancy and training

Requirements
Must have
• Name and contact details director: Clara Hotham, chotham@bag-example.co.nz, PO Box 419, Warkworth, NZ, cell +6427390516

```html
<!DOCTYPE html>
<html lang="en">
<head>
<meta charset="utf-8">
<title>Birchmead Assurance Group Ltd – Business Card</title>
<link href="https://fonts.googleapis.com/css2?family=Open+Sans:wght@400;600;700&display=swap" rel="stylesheet">
<style>
  :root {
    --page-bg: #ecebe8;
    --card-white: #ffffff;
    --brand-green-light: #6cb52d;
    --brand-green-dark: #0f7a12;
    --brand-green-text: #3f9a22;
    --ink-on-green: #ffffff;
    --card-shadow: 0 6px 22px rgba(0, 0, 0, 0.18);
  }
  * { box-sizing: border-box; margin: 0; padding: 0; }
  html, body {
    width: 1200px;
    height: 900px;
    overflow: hidden;
    background: var(--page-bg);
    font-family: "Open Sans", Arial, sans-serif;
  }
  .canvas { position: relative; width: 1200px; height: 900px; }

  .card {
    position: absolute;
    background: var(--card-white);
    box-shadow: var(--card-shadow);
  }
  .card--front { left: 78px; top: 34px; width: 588px; height: 364px; }
  .card--back  { left: 388px; top: 505px; width: 567px; height: 352px; }

  .green-band {
    position: absolute;
    left: 0;
    width: 100%;
    background: linear-gradient(to bottom, var(--brand-green-light), var(--brand-green-dark));
  }
  .card--front .green-band { top: 188px; height: 158px; }
  .card--back .green-band  { top: 110px; height: 131px; }

  .wordmark {
    position: absolute;
    left: 0;
    width: 100%;
    text-align: center;
    font-weight: 600;
    white-space: nowrap;
  }
  .card--front .wordmark { top: 96px; font-size: 30px; color: var(--brand-green-text); }
  .card--back .wordmark  { top: 46px; font-size: 29px; color: var(--ink-on-green); }

  .contact-lines {
    position: absolute;
    right: 322px;
    top: 26px;
    text-align: right;
    color: var(--ink-on-green);
    font-size: 15px;
    line-height: 26px;
  }
  .contact-line { display: flex; align-items: center; justify-content: flex-end; gap: 8px; }
  .contact-line svg { width: 11px; height: 11px; fill: var(--ink-on-green); }

  .person {
    position: absolute;
    left: 322px;
    top: 24px;
    color: var(--ink-on-green);
  }
  .person-name { font-size: 20px; font-weight: 700; line-height: 28px; }
  .person-role { font-size: 15px; line-height: 20px; }

  .postal-address {
    position: absolute;
    left: 0;
    top: 108px;
    width: 100%;
    padding-left: 8px;
    text-align: center;
    font-size: 15px;
    color: var(--ink-on-green);
  }
</style>
</head>
<body>
<main class="canvas">

  <section class="card card--front" aria-label="Business card front">
    <div class="wordmark">Birchmead Assurance Group Ltd</div>
    <div class="green-band">
      <div class="contact-lines">
        <div class="contact-line">
          <span>+6427390516</span>
          <svg viewBox="0 0 24 24" aria-hidden="true"><path d="M6.6 10.8a15.1 15.1 0 0 0 6.6 6.6l2.2-2.2a1 1 0 0 1 1-.25 11.4 11.4 0 0 0 3.6.57 1 1 0 0 1 1 1V20a1 1 0 0 1-1 1A17 17 0 0 1 3 4a1 1 0 0 1 1-1h3.5a1 1 0 0 1 1 1c0 1.25.2 2.45.57 3.57a1 1 0 0 1-.25 1z"/></svg>
        </div>
        <div class="contact-line">
          <span>chotham@bag-example.co.nz</span>
          <svg viewBox="0 0 24 24" aria-hidden="true"><path d="M2 5h20v14H2z M3.5 6.5 12 13l8.5-6.5" fill="none" stroke="#ffffff" stroke-width="2.4"/><rect x="2" y="5" width="20" height="14" fill="#ffffff"/><path d="M2 5l10 8 10-8" fill="none" stroke="#2d8f1a" stroke-width="2"/></svg>
        </div>
      </div>
      <div class="person">
        <div class="person-name">Clara Hotham</div>
        <div class="person-role">Director</div>
      </div>
      <div class="postal-address">PO Box 419, Warkworth, NZ</div>
    </div>
  </section>

  <section class="card card--back" aria-label="Business card back">
    <div class="green-band">
      <div class="wordmark">Birchmead Assurance Group Ltd</div>
    </div>
  </section>

</main>
</body>
</html>
```